Creative, Innovative PowerPoint Sales Deck Refresh needed

We are a technology firm in the Dallas, TX area and we need the powerpoint presentation used for our sales calls refreshed. This presentation is used in one of the first meetings we have with potential clients, so we want to make a memorable and positive impact - we want something that sets us apart from everyone else. We need 8 master slide templates created for our sales deck and a series of slides within the example sales deck need to be completely refreshed (slides 31-37 and 43 in the sample ppt file) We want a sales deck that is modern, innovative, creative, memorable and whimsical - NOT a typical boring "business" design. Colors should match or compliment the colors used in our logo. The logo in the footer of the attached sample ppt is old - it should be replaced with the newer logo attached. Please take a look at our website to get an idea of our culture and aesthetic www.quorbinlab.com
Updates

Project Deadline Extended
Reason: We have received several designs we like and we want our entire team to have time to give them full consideration before making a decision.

Target Market(s)

Business executives

Industry/Entity Type

Information Technology

Font styles to use
Sans Serif

Requirements
Must have
• Our logo and LedgerWave logo in footer
• Master Slide Templates
• Rework / redesign of slides 31-37 and 43
Nice to have
• We use Raleway font in a lot of our materials

```html
<!DOCTYPE html>
<html lang="en">
<head>
<meta charset="utf-8">
<title>Phase One Methodology – Slides 32 to 37</title>
<link href="https://fonts.googleapis.com/css2?family=Arimo:wght@400;700&family=Raleway:wght@400;500;600&display=swap" rel="stylesheet">
<style>
  :root{
    --canvas:#141a31;
    --title:#9aaba8;
    --brand-blue:#0b63b0;
    --cyl-top:#5fa3d6;
    --chevron:#a7a9ac;
    --heading:#4a4a4a;
    --rule:#d7dde6;
    --panel-dark:#3a3536;
    --panel-navy:#1f3864;
    --icon:#b9b9bb;
    --white:#ffffff;
    --ink:#2b2b2b;
  }
  *{box-sizing:border-box;margin:0;padding:0}
  html,body{width:1200px;height:1200px;overflow:hidden;background:var(--canvas)}
  .canvas{position:relative;width:1200px;height:1200px}
  .sheet-title{position:absolute;top:40px;left:0;width:100%;text-align:center;
    font-family:"Arimo",sans-serif;font-size:29px;color:var(--title);letter-spacing:.3px}
  .slide{position:absolute;width:590px;height:330px;background:var(--white);
    border-top:6px solid var(--brand-blue);overflow:hidden}
  .slide h2{position:absolute;left:18px;top:8px;width:554px;padding-bottom:5px;
    border-bottom:1px solid var(--rule);font-family:"Arimo",sans-serif;font-weight:700;
    font-size:17px;color:var(--heading)}
  .chevrons{position:absolute;left:36px;top:58px;width:516px;height:37px}
  .chevrons text{font-family:"Arimo",sans-serif;font-weight:700;font-size:12px;fill:var(--white);text-anchor:middle}
  .phase-icons{position:absolute;left:36px;top:118px;width:516px;height:40px}
  .cylinders{position:absolute;left:0;top:185px;width:590px;height:105px}
  .cylinders text{font-family:"Arimo",sans-serif;font-weight:700;font-size:11px;fill:var(--white);text-anchor:middle}
  .tag{position:absolute;left:28px;top:152px;width:142px;height:31px;background:var(--brand-blue);
    clip-path:polygon(0 0,88% 0,100% 50%,88% 100%,0 100%);color:var(--white);
    font-family:"Arimo",sans-serif;font-weight:700;font-size:12px;display:flex;align-items:center;
    justify-content:center;padding-right:12px;text-align:center;line-height:1.1}
  .panel{position:absolute;left:185px;top:148px;width:370px;height:125px;background:var(--panel-navy);
    border-radius:14px}
  .panel.wide{width:380px}
  .panel-icon{position:absolute;left:0;top:0;width:110px;height:125px;background:var(--panel-dark);
    border-radius:14px;display:flex;align-items:center;justify-content:center}
  .panel ul{position:absolute;left:128px;right:8px;top:0;bottom:0;display:flex;flex-direction:column;
    justify-content:center;gap:8px;list-style:none;font-family:"Raleway",sans-serif;font-size:10.5px;color:var(--white)}
  .panel li{position:relative;padding-left:12px}
  .panel li::before{content:"•";position:absolute;left:0}
  .panel li.sub{padding-left:48px;font-size:8.5px;margin-top:-2px}
  .panel li.sub::before{content:"-";left:38px}
  .panel ul.dense{gap:4px}
  .footer-left{position:absolute;left:20px;bottom:8px;font-family:"Arimo",sans-serif;font-size:14px;color:var(--ink)}
  .footer-right{position:absolute;right:18px;bottom:9px;display:flex;align-items:center;gap:5px;
    font-family:"Arimo",sans-serif;font-weight:700;font-size:11px;color:var(--ink);letter-spacing:.5px}
  .footer-right .mark{width:14px;height:14px;background:var(--panel-navy)}
</style>
</head>
<body>
<svg width="0" height="0" style="position:absolute">
  <defs>
    <polygon id="chev" points="0,0 94,0 112,18.5 94,37 0,37 18,18.5" fill="var(--chevron)"/>
    <g id="ic-monitor">
      <circle cx="18" cy="18" r="17" fill="#8f8f91" stroke="#d4d4d4" stroke-width="2"/>
      <rect x="9" y="10" width="18" height="12" rx="1" fill="none" stroke="#fff" stroke-width="2"/>
      <rect x="13" y="25" width="10" height="2" fill="#fff"/><rect x="17" y="22" width="2" height="3" fill="#fff"/>
    </g>
    <g id="ic-doc" fill="none" stroke="currentColor" stroke-width="2">
      <path d="M6 3h16v30H6z" fill="currentColor" stroke="none"/>
      <path d="M10 10h10M10 15h10M10 20h6" stroke="#fff"/>
      <path d="M18 30l10-10 4 4-10 10h-4z" fill="currentColor" stroke="#fff" stroke-width="1.5"/>
    </g>
    <g id="ic-code" fill="none" stroke="currentColor" stroke-width="1.5">
      <rect x="3" y="6" width="30" height="24"/><path d="M3 11h30"/>
      <circle cx="6" cy="8.5" r=".8"/><circle cx="9" cy="8.5" r=".8"/><circle cx="12" cy="8.5" r=".8"/>
      <path d="M13 16l-4 4 4 4M23 16l4 4-4 4M20 15l-4 10"/>
    </g>
    <g id="ic-gear" fill="none" stroke="currentColor" stroke-width="2">
      <path d="M16 4h12l6 6v22H16z"/><path d="M28 4v6h6"/>
      <circle cx="12" cy="26" r="4.5" fill="#fff"/>
      <circle cx="12" cy="26" r="7" stroke-dasharray="3 2.5" stroke-width="3"/>
    </g>
    <g id="ic-support" fill="none" stroke="currentColor" stroke-width="1.5">
      <rect x="2" y="6" width="26" height="18"/><path d="M2 10h26M6 15h10M6 19h8"/>
      <path d="M10 27h14"/>
      <circle cx="31" cy="19" r="5" fill="currentColor"/>
      <path d="M22 34c1-6 5-8 9-8s8 2 9 8z" fill="currentColor"/>
    </g>
  </defs>
</svg>

<div class="canvas">
  <h1 class="sheet-title">SLIDES - 32 to 37 ( Design Idea - 01)</h1>

  <!-- Overview -->
  <section class="slide" style="left:6px;top:138px">
    <h2>PHASE ONE METHODOLOGY</h2>
    <svg class="chevrons" viewBox="0 0 516 37" style="top:70px">
      <use href="#chev"/><use href="#chev" x="101"/><use href="#chev" x="202"/><use href="#chev" x="303"/><use href="#chev" x="404"/>
      <text x="60" y="15">Project</text><text x="60" y="29">Initiation</text>
      <text x="161" y="15">Solution</text><text x="161" y="29">Design</text>
      <text x="262" y="15">Application</text><text x="262" y="29">Configuration</text>
      <text x="363" y="15">Testing &amp;</text><text x="363" y="29">Preparation</text>
      <text x="464" y="15">Deployment</text><text x="464" y="29">&amp; Support</text>
    </svg>
    <svg class="phase-icons" viewBox="0 0 516 40" style="color:#8f8f91">
      <use href="#ic-monitor" x="42" y="2"/>
      <use href="#ic-doc" x="145" y="2"/>
      <use href="#ic-code" x="245" y="2"/>
      <use href="#ic-gear" x="345" y="2"/>
      <use href="#ic-support" x="445" y="2"/>
    </svg>
    <svg class="cylinders" viewBox="0 0 590 105">
      <g>
        <path d="M80 11v78a66 11 0 0 0 132 0V11z" fill="var(--brand-blue)"/>
        <ellipse cx="146" cy="11" rx="66" ry="11" fill="var(--cyl-top)"/>
        <text x="146" y="54">CHANGE</text><text x="146" y="67">MANAGEMENT</text>
      </g>
      <g>
        <path d="M229 11v78a66 11 0 0 0 132 0V11z" fill="var(--brand-blue)"/>
        <ellipse cx="295" cy="11" rx="66" ry="11" fill="var(--cyl-top)"/>
        <text x="295" y="54">USER</text><text x="295" y="67">INVOLVEMENT</text>
      </g>
      <g>
        <path d="M378 11v78a66 11 0 0 0 132 0V11z" fill="var(--brand-blue)"/>
        <ellipse cx="444" cy="11" rx="66" ry="11" fill="var(--cyl-top)"/>
        <text x="444" y="54">PROGRAM</text><text x="444" y="67">MANAGEMENT</text>
      </g>
    </svg>
    <div class="footer-left">quorbinlab</div>
    <div class="footer-right"><span class="mark"></span>LEDGERWAVE</div>
  </section>

  <!-- Project Initiation -->
  <section class="slide" style="left:605px;top:133px">
    <h2>PHASE ONE METHODOLOGY</h2>
    <svg class="chevrons" viewBox="0 0 516 37">
      <use href="#chev"/><use href="#chev" x="101"/><use href="#chev" x="202"/><use href="#chev" x="303"/><use href="#chev" x="404"/>
      <text x="60" y="15">Project</text><text x="60" y="29">Initiation</text>
    </svg>
    <div class="tag">Project Initiation</div>
    <div class="panel">
      <div class="panel-icon"><svg width="40" height="40" viewBox="0 0 36 36"><use href="#ic-monitor"/></svg></div>
      <ul>
        <li>Conduct Kickoff Meeting</li>
        <li>Finalize and Publish Project Schedule</li>
        <li>Requirements Definition and Design</li>
        <li>Requirements Traceability Matrix (RTM) Signoff</li>
      </ul>
    </div>
    <div class="footer-left">quorbinlab</div>
    <div class="footer-right"><span class="mark"></span>LEDGERWAVE</div>
  </section>

  <!-- Solution Design -->
  <section class="slide" style="left:5px;top:488px">
    <h2>PHASE ONE METHODOLOGY</h2>
    <svg class="chevrons" viewBox="0 0 516 37">
      <use href="#chev"/><use href="#chev" x="101"/><use href="#chev" x="202"/><use href="#chev" x="303"/><use href="#chev" x="404"/>
      <text x="161" y="15">Solution</text><text x="161" y="29">Design</text>
    </svg>
    <div class="tag">Solution Design</div>
    <div class="panel">
      <div class="panel-icon" style="color:var(--icon)"><svg width="38" height="38" viewBox="0 0 36 36"><use href="#ic-doc"/></svg></div>
      <ul class="dense">
        <li>Map and Gap Against RTM</li>
        <li>Identify Solutions for Gaps</li>
        <li class="sub">Custom Development</li>
        <li class="sub">Phase Two Initiative</li>
        <li class="sub">Business Process Change</li>
        <li>Business Flow Recommendation</li>
      </ul>
    </div>
    <div class="footer-left">quorbinlab</div>
    <div class="footer-right"><span class="mark"></span>LEDGERWAVE</div>
  </section>

  <!-- Application Testing -->
  <section class="slide" style="left:605px;top:488px">
    <h2>PHASE ONE METHODOLOGY</h2>
    <svg class="chevrons" viewBox="0 0 516 37">
      <use href="#chev"/><use href="#chev" x="101"/><use href="#chev" x="202"/><use href="#chev" x="303"/><use href="#chev" x="404"/>
      <text x="262" y="15">Application</text><text x="262" y="29">Testing</text>
    </svg>
    <div class="tag">Application Testing</div>
    <div class="panel">
      <div class="panel-icon" style="color:var(--icon)"><svg width="38" height="38" viewBox="0 0 36 36"><use href="#ic-code"/></svg></div>
      <ul>
        <li>System Setup</li>
        <li>Extended Prototyping</li>
        <li>Develop Test Scripts</li>
        <li>Initiate Data Cleansing and Conversion Routines</li>
      </ul>
    </div>
    <div class="footer-left">quorbinlab</div>
    <div class="footer-right"><span class="mark"></span>LEDGERWAVE</div>
  </section>

  <!-- Testing & Preparation -->
  <section class="slide" style="left:5px;top:835px">
    <h2>PHASE ONE METHODOLOGY</h2>
    <svg class="chevrons" viewBox="0 0 516 37">
      <use href="#chev"/><use href="#chev" x="101"/><use href="#chev" x="202"/><use href="#chev" x="303"/><use href="#chev" x="404"/>
      <text x="363" y="15">Testing &amp;</text><text x="363" y="29">Preparation</text>
    </svg>
    <div class="tag">Testing &amp; Preparation</div>
    <div class="panel wide" style="left:182px">
      <div class="panel-icon" style="color:var(--icon)"><svg width="38" height="38" viewBox="0 0 36 36"><use href="#ic-gear"/></svg></div>
      <ul>
        <li>Unit Testing – Individual modules/functions</li>
        <li>Integration Testing – End-to-End Flow (Order to Cash)</li>
        <li>User Acceptance Testing – Mock Go-Live</li>
        <li>Full Life Cycle Simulations</li>
        <li>End User Training</li>
      </ul>
    </div>
    <div class="footer-left">quorbinlab</div>
    <div class="footer-right"><span class="mark"></span>LEDGERWAVE</div>
  </section>

  <!-- Deployment & Support -->
  <section class="slide" style="left:605px;top:835px">
    <h2>PHASE ONE METHODOLOGY</h2>
    <svg class="chevrons" viewBox="0 0 516 37">
      <use href="#chev"/><use href="#chev" x="101"/><use href="#chev" x="202"/><use href="#chev" x="303"/><use href="#chev" x="404"/>
      <text x="464" y="15">Deployment</text><text x="464" y="29">&amp; Support</text>
    </svg>
    <div class="tag">Deployment &amp;<br>Support</div>
    <div class="panel wide" style="left:182px">
      <div class="panel-icon" style="color:var(--icon)"><svg width="44" height="40" viewBox="0 0 42 36"><use href="#ic-support"/></svg></div>
      <ul>
        <li>Setup Production Environment</li>
        <li>Convert Live Data</li>
        <li>GO-LIVE!</li>
        <li>Post Go-Live Support</li>
        <li>Project Closeout</li>
      </ul>
    </div>
    <div class="footer-left">quorbinlab</div>
    <div class="footer-right"><span class="mark"></span>LEDGERWAVE</div>
  </section>
</div>
</body>
</html>
```